Design a Cover for a Book on Innovation

I need a design for my book: The Quiet Orchard of Invention
It is about the following:

Innovation is not just for those endowed with special talent or skills in technology. This book describes the thought framework that consists of seven principal differences between the current period and the past. Innovation is happening along these shifts. Understanding the differences can allow for consistent innovation and the identification of real opportunities.
Updates

To All: All of you show great talent as designers. I've added a bit more to the description. Feel free to ask questions. Best, RT

Font styles to use
Sans Serif

Colors

Designer to choose colors to be used in the design.

Requirements
Must have
• It should feel modern and innovative. It should incorporate the meaning of Quiet Orchard.
Nice to have
• It should have the title, and a holder spot for the subtitle and author's name Rosa Ven Toh
Should not have
• It should not be overly busy. Sleek modern design that still gets the point across. Alternatively an image that is a full cover graphic.

```html
<!DOCTYPE html>
<html lang="en">
<head>
<meta charset="utf-8">
<title>The Quiet Orchard of Invention – Cover Variants</title>
<link rel="stylesheet" href="https://fonts.googleapis.com/css2?family=Poppins:wght@300;400&family=Raleway:ital,wght@0,500;1,400&display=swap">
<style>
  :root {
    --page-bg: #ffffff;
    --cover-bg: #fafaf9;
    --ink: #2f2f2f;
    --accent-orange: #f26a3d;
    --accent-crimson: #a1121b;
    --leaf-green-soft: rgba(111, 154, 46, 0.28);
    --glass: rgba(210, 225, 220, 0.35);
    --shadow: rgba(0, 0, 0, 0.28);
  }
  * { margin: 0; padding: 0; box-sizing: border-box; }
  html, body {
    width: 1200px;
    height: 774px;
    overflow: hidden;
    background: var(--page-bg);
  }
  .canvas {
    position: relative;
    width: 1200px;
    height: 774px;
  }
  .cover {
    position: absolute;
    top: 78px;
    width: 476px;
    height: 616px;
    background: var(--cover-bg);
    box-shadow: 4px 4px 7px var(--shadow);
    overflow: hidden;
  }
  .cover--orange { left: 110px; --accent: var(--accent-orange); }
  .cover--crimson { left: 616px; --accent: var(--accent-crimson); }

  .art-bulb-cluster {
    position: absolute;
    left: 86px;
    top: 0;
    width: 310px;
    height: 190px;
    background: linear-gradient(180deg, var(--leaf-green-soft) 0%, var(--glass) 60%, rgba(250, 250, 249, 0) 100%);
  }
  .art-sprouting-bulb {
    position: absolute;
    left: 272px;
    top: 190px;
    width: 70px;
    height: 244px;
    background: linear-gradient(180deg, rgba(250, 250, 249, 0) 0%, var(--leaf-green-soft) 55%, var(--glass) 100%);
    border-radius: 0 0 35px 35px;
  }

  .title {
    position: absolute;
    right: 211px;
    top: 246px;
    text-align: right;
    font-family: "Poppins", sans-serif;
    font-weight: 300;
    color: var(--ink);
    line-height: 1;
  }
  .title span { display: block; }
  .title__small { font-size: 27px; height: 29px; }
  .title__accent { font-size: 36px; height: 46px; padding-top: 4px; color: var(--accent); font-weight: 400; }
  .title__joiner { font-size: 27px; height: 30px; }
  .title__lead { font-size: 45px; color: var(--accent); letter-spacing: 0.2px; }

  .subtitle {
    position: absolute;
    left: 0;
    width: 474px;
    top: 466px;
    text-align: center;
    font-family: "Raleway", sans-serif;
    font-style: italic;
    font-weight: 400;
    font-size: 12.5px;
    color: var(--ink);
    text-transform: uppercase;
  }
  .author {
    position: absolute;
    left: 0;
    width: 446px;
    top: 548px;
    text-align: center;
    font-family: "Raleway", sans-serif;
    font-weight: 500;
    font-size: 12.5px;
    color: var(--ink);
    text-transform: uppercase;
  }
</style>
</head>
<body>
<main class="canvas">
  <article class="cover cover--orange">
    <div class="art-bulb-cluster" role="img" aria-label="Glass light bulbs with green caps hanging on green stems"></div>
    <div class="art-sprouting-bulb" role="img" aria-label="A long-stemmed glass bulb with a green leaf sprouting from its stem"></div>
    <h1 class="title">
      <span class="title__small">The</span>
      <span class="title__small">Quiet</span>
      <span class="title__accent">Orchard</span>
      <span class="title__joiner">of</span>
      <span class="title__lead">Invention</span>
    </h1>
    <p class="subtitle">A quiet guide to seeing what comes next</p>
    <p class="author">Rosa Ven Toh</p>
  </article>

  <article class="cover cover--crimson">
    <div class="art-bulb-cluster" role="img" aria-label="Glass light bulbs with green caps hanging on green stems"></div>
    <div class="art-sprouting-bulb" role="img" aria-label="A long-stemmed glass bulb with a green leaf sprouting from its stem"></div>
    <h1 class="title">
      <span class="title__small">The</span>
      <span class="title__small">Quiet</span>
      <span class="title__accent">Orchard</span>
      <span class="title__joiner">of</span>
      <span class="title__lead">Invention</span>
    </h1>
    <p class="subtitle">A quiet guide to seeing what comes next</p>
    <p class="author">Rosa Ven Toh</p>
  </article>
</main>
</body>
</html>
```